Stage Design Company Business Card

We are looking to step up up our business card design for our team.

We are a Full service Design and Consultation company for Stage and TV with an emphasis in Theatrical Lighting.

We like our materials to be clean and modern with solid colors free of patterns and gradients. Our brand consists of 4 primary colors Purple, Black, Grey, and White. Provided is our Word Mark as well as our Symbol Logo.

We would like our cards to leave an impression beyond the information, show our attention to design and detail, and make our marks an easily recognized feature (together or apart) for our clients.

We need a warm approachable comfortable feel for some clients, and a professional flair for the board member type clients.

Attached are our brand elements, and our existing cards to give a sense of our style and a glipse at the information we provide on our cards.

Target Market(s)

broad client base from church leaders to high school teachers and architects.

Industry/Entity Type

Business

Contact Information for Business Card

We format our phone number with periods not parenthesis or dashes. Information will be edited for each of our team members, and team member specific cards are not part of this scope, but rather a template so to speak.

Font styles to use
Sans Serif

Colors
6b449b
ffffff
000000
333333
aaaaaa

Requirements
Must have
• Wordmark and logo mark present (does not need to exist on the same side of card)
• Brand Colors,
• Name, Phone, Email, Address.
• Unique choices that make someone stop and take a second look
Nice to have
• It would be nice to somehow convey what we DO, as our brand name does not lend itself to this, outside of an obvious tagline though.....
• social media if not crowded. all of our handles match (instagram, twitter, facebook)
Should not have
• "clipart"

```html
<!DOCTYPE html>
<html lang="en">
<head>
<meta charset="utf-8">
<title>Lumara Business Card</title>
<link rel="stylesheet" href="https://fonts.googleapis.com/css2?family=Open+Sans:wght@400;600;700&display=swap">
<style>
  :root {
    --purple: #3a2778;
    --charcoal: #2c2c2e;
    --ink: #1d1d1f;
    --paper: #ffffff;
    --muted: #d9d9dc;
    --backdrop: #e9e8ec;
  }
  * { box-sizing: border-box; margin: 0; padding: 0; }
  html, body {
    width: 1200px; height: 899px; overflow: hidden;
    background: var(--backdrop);
    font-family: "Open Sans", sans-serif;
  }
  .sheet { position: relative; width: 1200px; height: 899px; }
  .card {
    position: absolute; left: 240px; width: 720px; height: 411px;
    box-shadow: 0 6px 18px rgba(0,0,0,.18);
    overflow: hidden;
  }
  .card--back { top: 26px; background: var(--charcoal); color: var(--muted); }
  .card--front { top: 462px; background: var(--paper); color: var(--ink); }

  .brand { display: flex; align-items: center; gap: 26px; }
  .brand__dot { width: 58px; height: 58px; border-radius: 50%; }
  .brand__name { font-weight: 600; letter-spacing: 22px; line-height: 1; }

  .card--back .brand { position: absolute; left: 212px; top: 118px; }
  .card--back .brand__dot { background: var(--paper); }
  .card--back .brand__name { color: var(--paper); font-size: 40px; }
  .tagline {
    position: absolute; left: 0; right: 0; top: 250px;
    text-align: center; font-size: 19px; line-height: 1.35; font-weight: 400;
  }

  .card__band { position: absolute; left: 0; bottom: 0; width: 720px; height: 120px; }
  .holder { position: absolute; left: 24px; top: 24px; display: flex; gap: 12px; }
  .holder__mark { width: 46px; height: 46px; }
  .holder__name { color: var(--purple); font-weight: 700; font-size: 25px; line-height: 1.1; }
  .holder__role { font-size: 15px; margin-top: 2px; }

  .contact { position: absolute; left: 34px; top: 140px; font-size: 17px; line-height: 1.38; }
  .contact__address { margin-bottom: 4px; }
  .contact__line { display: flex; align-items: center; gap: 9px; }
  .contact__icon { width: 14px; height: 14px; flex: none; }

  .card--front .brand { position: absolute; left: 360px; top: 156px; gap: 22px; }
  .card--front .brand__dot { width: 50px; height: 50px; background: var(--purple); }
  .card--front .brand__name { color: var(--purple); font-size: 36px; letter-spacing: 18px; }
</style>
</head>
<body>
<main class="sheet">

  <section class="card card--back">
    <div class="brand">
      <span class="brand__dot"></span>
      <span class="brand__name">LUMARA</span>
    </div>
    <p class="tagline">Design and Consultation company for Stage<br>and TV with an emphasis in Theatrical Lighting.</p>
  </section>

  <section class="card card--front">
    <div class="holder">
      <svg class="holder__mark" viewBox="0 0 46 46" aria-hidden="true">
        <rect width="46" height="46" fill="var(--purple)"/>
        <polygon points="30,0 34,0 4,46 0,46" fill="var(--paper)"/>
      </svg>
      <div>
        <p class="holder__name">Marcus Ellery</p>
        <p class="holder__role">Managing Director</p>
      </div>
    </div>

    <div class="contact">
      <p class="contact__address">48 Harbor Lane, Suite 12<br>Westfield, 402176.</p>
      <p class="contact__line">
        <svg class="contact__icon" viewBox="0 0 16 16" aria-hidden="true"><path d="M3 1h3l1.5 4-2 1.3a9 9 0 0 0 4.2 4.2L11 8.5l4 1.5v3c0 1-1 2-2 2A12 12 0 0 1 1 3c0-1 1-2 2-2z" fill="var(--purple)"/></svg>
        044.555.0172
      </p>
      <p class="contact__line">
        <svg class="contact__icon" viewBox="0 0 16 16" aria-hidden="true"><rect x="1" y="3" width="14" height="10" fill="var(--purple)"/><polyline points="1,3 8,9 15,3" fill="none" stroke="var(--paper)" stroke-width="1.4"/></svg>
        hello@lumara.com
      </p>
      <p class="contact__line">
        <svg class="contact__icon" viewBox="0 0 16 16" aria-hidden="true"><g fill="none" stroke="var(--purple)" stroke-width="2"><rect x="1.5" y="6" width="8" height="4" rx="2" transform="rotate(-45 5.5 8)"/><rect x="6.5" y="6" width="8" height="4" rx="2" transform="rotate(-45 10.5 8)"/></g></svg>
        www.lumarastage.com
      </p>
    </div>

    <div class="brand">
      <span class="brand__dot"></span>
      <span class="brand__name">LUMARA</span>
    </div>

    <svg class="card__band" viewBox="0 0 720 120" aria-hidden="true">
      <polygon points="0,38 250,78 250,96 0,96" fill="var(--purple)"/>
      <polygon points="270,82 720,82 720,120 246,120" fill="var(--purple)"/>
    </svg>
  </section>

</main>
</body>
</html>
```